Redesign criminal justice consulting website

We run a small professional services firm that does research, evaluation, consulting, and training on criminal justice issues. We need to redesign our website (www.rvmetrics.com). The existing site is something we made ourselves. It is unprofessional and does not do a good job of communicating what we do or who we are.

We would like the new site to provide a basic overview of what we do. Moreover, we would like it to communicate several themes that represent who we are:

* global

* innovative

* analytical

* practical

We view the principal design challenge as figuring out a subtle, interesting, and graphically appealing way to communicate these themes.

Target Market(s)

Our primary customers are governments, research firms, criminal justice agencies, and schools. The people who we want to find our site are seeking research, evaluation, training, or consulting services related to crime, criminal justice, or policing.

Industry/Entity Type

Consulting

Number of Pages Required

2 pages

Requirements
Must have
• 1. We would like the site to use our logo. It is attached (please use the maroon 4-color version with the company name but without the slogan). The site should also use the colors present in our logo. It may use other colors as well, as long as these colors coordinate with the logo colors.

• 2. For main pages or buttons, we need the following:
• *Home
• *About RVM
• *Services
• *E-Training
• *Resources
• *Contact RVM

• 3. We like simple, crisp, subtle designs over "busier," cluttered, or very complex designs.

• 4. We'd like to receive, at a minimum, the home page and a sample inner page.
Nice to have
• We need some help in thinking through what regions or sections should exist on the home page. We are thinking about having a window on there where we can make announcements about recent developments like new reports, new e-training videos, new photographs, etc... We are open to suggestions here.
Should not have
• 1. Gimmicky or overused clipart.
• 2. Cliched images associated with criminal justice, including magnifying glasses, scales of justice, etc... Our logo makes a subtle nod to criminal justice through the use of a fingerprint as the dot on the "J" in the company initials. That''s sufficient for our purposes. Concentrate instead on the themes listed above.
• 3. Major use of colors that don't match our logo, like blue.

```html
<!DOCTYPE html>
<html lang="en">
<head>
<meta charset="utf-8">
<title>RVM – Home and About</title>
<link href="https://fonts.googleapis.com/css2?family=Arimo:wght@400;700&display=swap" rel="stylesheet">
<style>
:root{
  --maroon:#a3270a;
  --maroon-dark:#7c1b03;
  --accent:#c0270a;
  --ink:#111;
  --body:#6a6a6a;
  --grey-band:#e4e4e4;
  --grey-panel:#f4f4f4;
  --grey-footer:#e6e6e6;
  --grey-divider:#c7c7c7;
  --black:#000;
  --white:#fff;
}
*{margin:0;padding:0;box-sizing:border-box}
html,body{width:1200px;height:2613px;overflow:hidden;background:var(--white)}
body{font-family:"Arimo",Arial,sans-serif;color:var(--body);position:relative}
.page{position:absolute;left:0;width:1200px}
.page--home{top:0;height:1320px;background:var(--white)}
.page--about{top:1320px;height:1293px;background:var(--white)}

/* header */
.brand{position:absolute;left:40px;top:28px;display:flex;align-items:center;gap:14px}
.brand__mark{width:18px;height:18px;background:var(--maroon)}
.brand__name{font-size:70px;font-weight:700;color:var(--maroon);letter-spacing:-2px;line-height:1}

/* nav */
.nav{position:absolute;left:0;width:1200px;height:46px;
  background:linear-gradient(var(--maroon) 0%,var(--maroon-dark) 100%);
  border-top:3px solid #c24a2c}
.nav ul{list-style:none;display:flex;position:absolute;left:40px;width:1120px;height:100%}
.nav li{flex:1;display:flex;align-items:center;justify-content:center;position:relative;
  color:var(--white);font-size:13px;font-weight:700;text-transform:uppercase;letter-spacing:.3px}
.nav li.is-active{background:var(--black)}
.nav li.is-active::after{content:"";position:absolute;left:50%;bottom:-10px;margin-left:-10px;
  border-left:10px solid transparent;border-right:10px solid transparent;border-top:10px solid var(--black)}

.band{position:absolute;left:0;width:1200px;background:var(--grey-band)}
.sheet{position:absolute;left:40px;width:1120px;background:var(--white)}

/* hero */
.hero{position:absolute;left:40px;top:227px;width:1120px;height:356px;
  background:linear-gradient(100deg,#57574f 0%,#6c6c63 45%,#85857c 100%)}
.hero__object{position:absolute;left:630px;top:18px;width:420px;height:316px;border-radius:20px;
  background:radial-gradient(ellipse at 50% 45%,#d9d9d6 0%,#a9a9a5 55%,rgba(120,120,114,0) 75%)}
.hero__text{position:absolute;left:48px;top:104px;width:560px;color:var(--white)}
.hero__title{font-size:38px;font-weight:700;margin-bottom:14px}
.hero__sub{font-size:23px;font-weight:700;margin-bottom:20px}
.hero__lede{font-size:14px;font-weight:700;line-height:17px}
.slider-bar{position:absolute;left:40px;top:583px;width:1120px;height:44px;background:var(--black)}
.slider-dots{position:absolute;right:60px;top:13px;display:flex;gap:3px}
.slider-dots span{width:14px;height:14px;border:1px solid var(--white)}
.slider-dots span.is-current{background:var(--white)}

/* home content */
.news{position:absolute;left:100px;top:670px;width:312px}
.news__title{font-size:28px;font-weight:400;color:var(--ink);letter-spacing:-.5px}
.news__title em{font-style:normal;color:var(--accent)}
.news__image{margin-top:14px;width:312px;height:168px;background:linear-gradient(135deg,#f1eeea,#c9c4bd)}
.news__head{margin-top:22px;font-size:17px;font-weight:700;color:var(--ink)}
.news__text{margin-top:10px;font-size:16px;line-height:20px}
.news__links{list-style:none;margin-top:38px}
.news__links li{font-size:17px;font-weight:700;color:var(--maroon);line-height:29.5px}
.news__links li::before{content:"»";color:var(--body);font-weight:400;margin-right:18px}

.feature{position:absolute;left:426px;top:647px;width:720px;height:560px;background:var(--grey-panel);padding:34px 40px}
.feature h2{font-size:17px;font-weight:700;color:var(--ink);margin-bottom:16px}
.feature p{font-size:16px;line-height:20px;margin-bottom:20px}
.feature .more{font-size:16px;font-weight:700;color:var(--accent)}

/* footer */
.footer{position:absolute;left:0;width:1200px;height:80px;background:var(--grey-footer);
  border-top:7px solid #d9d9d9;display:flex;align-items:center;justify-content:center;
  font-size:12px;color:#888;text-transform:uppercase}
.footer b{color:#777;margin-right:4px}
.footer .sep{margin-right:4px}
.divider{position:absolute;left:0;top:1297px;width:1200px;height:23px;background:var(--grey-divider)}

/* about */
.about__title{position:absolute;left:110px;top:272px;font-size:27px;font-weight:400;color:var(--accent)}
.about__photo{position:absolute;left:110px;top:323px;width:382px;height:256px;
  background:linear-gradient(180deg,#cfd5d8 0%,#8d8f92 55%,#2a2a2e 100%)}
.about__intro{position:absolute;left:520px;top:323px;width:590px}
.about__intro .lead{font-size:17px;font-weight:700;color:#444;line-height:20px;margin-bottom:18px}
.about__intro p{font-size:16px;line-height:19.5px;margin-bottom:18px}
.about__note{position:absolute;left:110px;top:600px;width:1000px;font-size:17px;font-weight:700;color:#444}
.about__sub{position:absolute;left:110px;top:688px;font-size:27px;font-weight:400;color:var(--accent)}
.about__body{position:absolute;left:110px;top:737px;width:1000px}
.about__body p{font-size:16px;line-height:19.5px;margin-bottom:20px;text-align:justify}
.about__body p.gap{margin-top:40px}
</style>
</head>
<body>

<section class="page page--home">
  <header class="brand"><span class="brand__mark"></span><span class="brand__name">RVM</span></header>
  <nav class="nav" style="top:162px">
    <ul>
      <li class="is-active">Home</li><li>About RVM</li><li>Services</li><li>E-Training</li><li>Resources</li><li>Contact RVM</li>
    </ul>
  </nav>
  <div class="band" style="top:211px;height:380px"></div>
  <div class="hero">
    <div class="hero__object" role="img" aria-label="Brushed metal puzzle piece photograph"></div>
    <div class="hero__text">
      <h1 class="hero__title">What we do?</h1>
      <p class="hero__sub">This is what we’re asked by many people.</p>
      <p class="hero__lede">Our clients know we suscipit nibh nisl vel enim ad duis vero ut in eum dolore magna zzril ut, consequat ex feugiat, quis, nostrud ea, vel.</p>
    </div>
  </div>
  <div class="slider-bar"><div class="slider-dots"><span class="is-current"></span><span></span><span></span><span></span></div></div>
  <div class="sheet" style="top:627px;height:590px"></div>

  <aside class="news">
    <h2 class="news__title">Whats <em>new!</em></h2>
    <div class="news__image" role="img" aria-label="Stack of folded newspapers"></div>
    <h3 class="news__head">Vel vulputate nulla et duis amet.</h3>
    <p class="news__text">Exerci nulla, in ipsum esse in ut, wisi nulla consequat eu wisi eum tincidunt vel nostrud.</p>
    <ul class="news__links">
      <li>Exerci nulla</li><li>In ipsum esse in</li><li>Wisi nulla consequat</li><li>Eu wisi eum</li><li>Tincidunt vel nostrud.</li>
    </ul>
  </aside>

  <article class="feature">
    <h2>Vel vulputate nulla et duis amet.</h2>
    <p>Exerci nulla, in ipsum esse in ut, wisi nulla consequat eu wisi eum tincidunt vel nostrud.</p>
    <p>Exerci nulla, in ipsum esse in ut, wisi nulla consequat eu wisi eum suscipit idunt vel nostrud at vulputate vel illum molestie minim commy consequat.</p>
    <p>Augue in laoreet, euismod nostrud iusto vel amet wisi iusto .</p>
    <p>Quis duis feugiat adipiscing ut. Lobortis, lobortis velit erat dolore qui. Blandit sit elit minim blandit ullamcorper.</p>
    <p>Augue in laoreet, euismod nostrud iusto vel amet wisi iusto quis duis feug adipiscing ut. Lobortis, lobortis velit er dolore qui.</p>
    <p>Blandit sit elit minim blandit ullamcorpe.</p>
    <span class="more">read more...</span>
  </article>

  <footer class="footer" style="top:1217px"><b>Copyright</b><span class="sep">|</span>All rights reserved</footer>
  <div class="divider"></div>
</section>

<section class="page page--about">
  <header class="brand"><span class="brand__mark"></span><span class="brand__name">RVM</span></header>
  <nav class="nav" style="top:162px">
    <ul>
      <li>Home</li><li class="is-active">About RVM</li><li>Services</li><li>E-Training</li><li>Resources</li><li>Contact RVM</li>
    </ul>
  </nav>
  <div class="band" style="top:208px;height:1008px"></div>
  <div class="sheet" style="top:228px;height:988px"></div>

  <h1 class="about__title">About RVM</h1>
  <div class="about__photo" role="img" aria-label="Photograph of a smiling team of four colleagues"></div>
  <div class="about__intro">
    <p class="lead">Consequat in feugiat eros duis amet, te, blandit, odio duis te illum aliquip duis aliquam consequat quis, diam vero.</p>
    <p>Exerci nulla, dolor lorem esse in facilisi, ut nulla consequat eu wisi eum ullamcorper euismod autem quis facilisis vulputate vel vel esse ad minim commodo.</p>
    <p>Autem, feugait enim minim vero commodo accumsan delenit ut illum sed vero, hendrerit ut suscipit velit vel, ullamcorper aliquip ea.</p>
    <p>Qui ea eum duis duis blandit dolor accumsan exerci enim nulla dignissim dolore aliquam nulla nibh et velit dolore aliquip consequat wisi ut.</p>
  </div>
  <p class="about__note">Ut in luptatum dolore dolor ullamcorper et molestie in laoreet, euismod nostrud.</p>

  <h2 class="about__sub">Vel duis</h2>
  <div class="about__body">
    <p>Vel duis, tincidunt feugait hendrerit iriure ipsum delenit, iriure, odio lobortis veniam, enim luptatum facilisi nulla volutpat. Elit, qui vel facilisis duis eu veniam duis, facilisi dolor feugiat, aliquip, ad lobortis, nonummy. Adipiscing amet, ut consectetuer nibh nostrud sed commodo esse, lobortis dolore praesent odio dolore, accumsan, iusto quis facilisis. Qui ea eum duis duis blandit dolor accumsan exerci enim nulla dignissim dolore aliquam nulla nibh et velit dolore aliquip consequat wisi ut. Duis autem te suscipit volutpat tation velit praesent eum magna, ipsum elit in consectetuer ut hendrerit exerci zzril. Lorem veniam molestie vero eros enim eu vulputate, ut eros nulla ea. Autem, feugait enim minim vero commodo accumsan delenit ut illum sed vero, hendrerit ut suscipit velit vel, ullamcorper aliquip ea.</p>
    <p>Praesent laoreet, euismod nostrud et vel sit ut iusto quis augue feugiat adipiscing ut. Lobortis, lobortis vulputate erat laoreet dignissim, qui dolor elit minim blandit tation. Eu at diam augue nostrud ex, tation, wisi, erat luptatum tation adipiscing, in. Consectetuer zzril nisl consequat accumsan tincidunt, feugait suscipit dolore nisl et at. Iusto, nisl nonummy molestie qui vel augue eum iriure vel wisi luptatum, lorem.</p>
    <p class="gap">Iusto dignissim dolore aliquam nulla nibh et velit dolore aliquip consequat wisi ut dolore autem te suscipit volutpat tation. Te praesent eum magna, ipsum elit in consectetuer ut hendrerit exerci zzril tation veniam molestie vero eros enim eu vulputate, ut eros nulla. Euismod exerci, feugait enim minim vero commodo accumsan delenit ut illum sed vero, hendrerit ut suscipit velit vel, ullamcorper aliquip ea. In praesent dolore veniam in odio duis, tincidunt feugait hendrerit iriure ipsum delenit, iriure, odio lobortis veniam, enim. Laoreet facilisi nulla volutpat consequat, qui vel facilisis duis eu veniam duis, facilisi dolor feugiat, aliquip, ad lobortis. Tation augue amet, ut consectetuer nibh nostrud sed commodo esse. Suscipit dolore praesent odio dolore, accumsan, iusto quis facilisis consequat ea eum duis.</p>
  </div>

  <footer class="footer" style="top:1216px;height:77px"><b>Copyright</b><span class="sep">|</span>All rights reserved</footer>
</section>

</body>
</html>
```